Branding Package
Business cards, stationery, envelopes, folders
Professional
Maureen Tolliver
Realtor
58 Birchwood St Suite 206 Lynn, MA 01905
maureen@korvastarealty.com
www.korvastarealty.com

```html
<!DOCTYPE html>
<html lang="en">
<head>
<meta charset="utf-8">
<title>Korvasta Realty — Branding Package</title>
<link href="https://fonts.googleapis.com/css2?family=Cormorant+Garamond:wght@500;600&family=Lato:wght@400;700&display=swap" rel="stylesheet">
<style>
  :root{
    --backdrop:#5b3d26;
    --paper:#ffffff;
    --gold:#c4a156;
    --gold-deep:#a8853f;
    --ink:#1d1a17;
    --muted:#6f665c;
    --watermark:#f1ebdf;
  }
  *{margin:0;padding:0;box-sizing:border-box}
  html,body{width:1200px;height:701px;overflow:hidden}
  body{background:var(--backdrop);position:relative;font-family:"Lato",sans-serif;color:var(--ink)}
  .piece{position:absolute;background:var(--paper);box-shadow:0 4px 14px rgba(0,0,0,.35)}
  .brand{font-family:"Cormorant Garamond",serif;font-weight:600;color:var(--ink);letter-spacing:.04em;line-height:1}
  .brand-dot{display:inline-block;width:.28em;height:.28em;border-radius:50%;background:var(--gold);vertical-align:middle;margin-left:.2em}
  .watermark{position:absolute;background:radial-gradient(ellipse at center,var(--watermark) 0%,rgba(241,235,223,0) 70%)}
  .small{font-size:7px;line-height:1.5;color:var(--muted)}
  .gold-rule{position:absolute;width:3px;background:var(--gold)}

  /* envelope back */
  .envelope-back{left:77px;top:185px;width:396px;height:200px;overflow:hidden}
  .envelope-back svg{position:absolute;left:0;top:0}
  .flap-mark{position:absolute;left:0;width:100%;top:34px;text-align:center;font-size:20px;color:var(--paper)}

  /* envelope front */
  .envelope-front{left:144px;top:312px;width:449px;height:204px;overflow:hidden}
  .envelope-front .brand{position:absolute;left:22px;top:30px;font-size:34px}
  .envelope-front .watermark{right:-20px;top:40px;width:180px;height:160px}
  .envelope-front .return{position:absolute;left:22px;top:160px}
  .envelope-front .gold-rule{left:0;top:160px;height:22px}

  /* letterhead */
  .letterhead{left:473px;top:19px;width:346px;height:576px;overflow:hidden}
  .letterhead .brand{position:absolute;left:22px;top:30px;font-size:34px}
  .letterhead .watermark{left:150px;top:20px;width:240px;height:420px}
  .letterhead .footer{position:absolute;left:22px;bottom:16px}
  .letterhead .gold-rule{left:0;bottom:16px;height:34px}

  /* business card front */
  .card-front{left:905px;top:499px;width:168px;height:96px;overflow:hidden}
  .card-front .brand{position:absolute;left:12px;top:12px;font-size:18px}
  .card-front .person{position:absolute;right:10px;top:40px;text-align:right}
  .card-front .person .name{font-size:8px;color:var(--gold-deep);font-weight:700}
  .card-front .contact{position:absolute;left:12px;bottom:8px;font-size:5.5px}
  .card-front .gold-rule{left:0;bottom:8px;height:20px}

  /* business card back */
  .card-back{left:1013px;top:413px;width:168px;height:96px;background:linear-gradient(135deg,var(--gold) 0%,var(--gold-deep) 100%);display:flex;align-items:center;justify-content:center}
  .card-back .brand{color:var(--paper);font-size:18px}
</style>
</head>
<body>

<section class="piece envelope-back" aria-label="Envelope back">
  <svg width="396" height="200" viewBox="0 0 396 200" aria-hidden="true">
    <polygon points="0,0 396,0 396,22 198,110 0,22" fill="var(--gold)"/>
    <line x1="0" y1="22" x2="198" y2="110" stroke="var(--gold-deep)" stroke-width="1"/>
    <line x1="396" y1="22" x2="198" y2="110" stroke="var(--gold-deep)" stroke-width="1"/>
  </svg>
  <div class="flap-mark brand">Korvasta</div>
</section>

<section class="piece envelope-front" aria-label="Envelope front">
  <div class="watermark" role="img" aria-label="Faint decorative flourish"></div>
  <div class="brand">Korvasta <span class="brand-dot"></span></div>
  <div class="gold-rule"></div>
  <div class="return small">58 Birchwood St Suite 206<br>Lynn, MA 01905</div>
</section>

<section class="piece letterhead" aria-label="Letterhead">
  <div class="watermark" role="img" aria-label="Large faint decorative flourish"></div>
  <div class="brand">Korvasta <span class="brand-dot"></span></div>
  <div class="gold-rule"></div>
  <div class="footer small">
    58 Birchwood St Suite 206 Lynn, MA 01905<br>
    Tel 781 555 0142 · Fax 781 555 0143<br>
    www.korvastarealty.com
  </div>
</section>

<section class="piece card-front" aria-label="Business card front">
  <div class="brand">Korvasta <span class="brand-dot"></span></div>
  <div class="person">
    <div class="name">Maureen Tolliver</div>
    <div class="small">Realtor</div>
  </div>
  <div class="gold-rule"></div>
  <div class="contact small">
    58 Birchwood St Suite 206 Lynn, MA 01905<br>
    Tel 781 555 0142 · maureen@korvastarealty.com
  </div>
</section>

<section class="piece card-back" aria-label="Business card back">
  <div class="brand">Korvasta</div>
</section>

</body>
</html>
```